Book cover for the book The Copper Lantern Beneath Harrow Lake

This is a 6x9 paperback book titled The Copper Lantern Beneath Harrow Lake: Field Notes on Tidal Rhythms from Sailors and Keepers Along the Northern Coast. It will be a cover full of love, reunion, and warmth. No ghosts, cemeteries, and so on. I'm open to any creative design. Might include someone rising in spirit from a sick bed to the welcoming arms of loved ones. Or someone being greeted by family in a scene of enchanting beauty that is the life after this life. The world of the life after this life is just like earth, except more beautiful, with colors we can't imagine, large flowers, opulent buildings, and people all young wearing robes of varying colors. No religious symbols. No sun, moon, or stars.

Font styles to use
Serif

Requirements
Should not have
• Cemeteries, ghosts, anything ghoulish and spooky

```html
<!DOCTYPE html>
<html lang="en">
<head>
<meta charset="utf-8">
<title>The Copper Lantern Beneath Harrow Lake — Cover Wrap</title>
<link rel="stylesheet" href="https://fonts.googleapis.com/css2?family=Cinzel:wght@400;500&family=Sorts+Mill+Goudy&display=swap">
<style>
  :root {
    --sky-light: #fef8c4;
    --sky-gold: #fbe27e;
    --haze-amber: #f6bf3a;
    --cloud-glow: #fde59a;
    --ridge-orange: #eb9a3a;
    --slope-rust: #c46a24;
    --valley-brown: #8a4a20;
    --summit-red: #7a1408;
    --summit-dark: #2c0704;
    --ink: #0f0d08;
    --author-gold: #f8de7a;
    --label-white: #ffffff;
  }
  * { margin: 0; padding: 0; box-sizing: border-box; }
  html, body { width: 1200px; height: 864px; overflow: hidden; background: var(--sky-light); }
  .cover-wrap {
    position: relative;
    width: 1200px;
    height: 864px;
    overflow: hidden;
    color: var(--ink);
    font-family: "Cinzel", "Times New Roman", serif;
  }
  .landscape-photo { position: absolute; inset: 0; }
  .landscape-photo .layer { position: absolute; inset: 0; }
  .sky-layer {
    background: linear-gradient(180deg, var(--sky-light) 0%, var(--sky-gold) 24%, var(--haze-amber) 38%, var(--cloud-glow) 45%, var(--ridge-orange) 52%, var(--slope-rust) 68%, var(--valley-brown) 86%, #6a3a1c 100%);
  }
  .haze-layer {
    background:
      radial-gradient(ellipse 300px 70px at 320px 330px, rgba(230,150,20,0.55), rgba(230,150,20,0) 100%),
      radial-gradient(ellipse 420px 160px at 940px 400px, rgba(255,248,210,0.8), rgba(255,248,210,0) 100%),
      radial-gradient(ellipse 600px 90px at 560px 440px, rgba(255,230,150,0.55), rgba(255,230,150,0) 100%);
  }
  .ridge-layer {
    background:
      radial-gradient(ellipse 520px 180px at 320px 600px, rgba(200,110,40,0.45), rgba(200,110,40,0) 100%),
      radial-gradient(ellipse 360px 200px at 1120px 560px, rgba(240,120,40,0.5), rgba(240,120,40,0) 100%);
  }
  .summit-layer {
    background:
      radial-gradient(ellipse 150px 110px at 930px 560px, rgba(140,40,12,0.9), rgba(140,40,12,0) 100%),
      radial-gradient(ellipse 560px 400px at 960px 920px, var(--summit-dark) 0%, var(--summit-red) 50%, rgba(160,50,15,0.55) 72%, rgba(160,50,15,0) 100%);
  }

  .title-line, .title-main, .subtitle-line, .author-line {
    position: absolute;
    white-space: nowrap;
    text-align: center;
    transform: translateX(-50%);
  }
  .title-line { font-weight: 400; text-transform: uppercase; line-height: 1; }
  .title-main { font-weight: 400; text-transform: uppercase; line-height: 1; }

  .back-title .title-line { left: 285px; font-size: 26px; }
  .back-title .title-main { left: 285px; font-size: 70px; }

  .front-title .title-line { left: 913px; font-size: 40px; }
  .front-title .title-main { left: 913px; font-size: 118px; }

  .subtitle-line {
    left: 913px;
    font-family: "Sorts Mill Goudy", "Georgia", serif;
    font-size: 26px;
    line-height: 1;
  }
  .author-line {
    left: 913px;
    color: var(--author-gold);
    font-size: 44px;
    line-height: 1;
    text-transform: uppercase;
  }

  .spine-title, .spine-author {
    position: absolute;
    left: 591px;
    writing-mode: vertical-rl;
    transform: rotate(180deg);
    white-space: nowrap;
    text-transform: uppercase;
    font-size: 19px;
    line-height: 22px;
  }
  .spine-title { top: 80px; color: var(--ink); }
  .spine-author { top: 638px; color: var(--author-gold); }

  .barcode-label {
    position: absolute;
    left: 311px;
    top: 735px;
    width: 213px;
    height: 101px;
    background: var(--label-white);
  }
</style>
</head>
<body>
  <div class="cover-wrap">
    <div class="landscape-photo" role="img" aria-label="Golden sunlit mountain range under a glowing hazy sky, with a figure raising both arms atop a dark rocky summit on the front cover">
      <div class="layer sky-layer"></div>
      <div class="layer haze-layer"></div>
      <div class="layer ridge-layer"></div>
      <div class="layer summit-layer"></div>
    </div>

    <section class="back-cover">
      <h2 class="back-title">
        <span class="title-line" style="top:33px">The Copper Lantern</span>
        <span class="title-line" style="top:65px">Beneath Harrow</span>
        <span class="title-main" style="top:88px">Lake</span>
      </h2>
      <div class="barcode-label"></div>
    </section>

    <section class="spine">
      <p class="spine-title">The Copper Lantern Beneath Harrow Lake</p>
      <p class="spine-author">Author Name</p>
    </section>

    <section class="front-cover">
      <h1 class="front-title">
        <span class="title-line" style="top:55px">The Copper Lantern</span>
        <span class="title-line" style="top:109px">Beneath Harrow</span>
        <span class="title-main" style="top:143px">Lake</span>
      </h1>
      <p class="front-subtitle">
        <span class="subtitle-line" style="top:260px">Field Notes on Tidal Rhythms from Sailors and</span>
        <span class="subtitle-line" style="top:297px">Keepers Along the Northern Coast</span>
      </p>
      <p class="front-author">
        <span class="author-line" style="top:732px">Author</span>
        <span class="author-line" style="top:788px">Name</span>
      </p>
    </section>
  </div>
</body>
</html>
```